TalkWell needs a Letterhead

We need a letterhead for our company "TalkWell Consultants". Logo is attached. The company color is Turquoise. Icons for website, scan logo for website, icons for address, e-mail and phone appreciated rather than just words.

```html
<!DOCTYPE html>
<html lang="en">
<head>
<meta charset="utf-8">
<title>TalkWell Consultants Letterhead</title>
<link rel="stylesheet" href="https://fonts.googleapis.com/css2?family=Arimo:ital,wght@0,400;1,400&family=Great+Vibes&display=swap">
<style>
  :root {
    --brand-blue: #3a9ad9;
    --brand-green: #4cc13a;
    --accent-orange: #e8743b;
    --ink: #333333;
    --ink-dark: #1a1a1a;
    --paper: #ffffff;
  }
  * { margin: 0; padding: 0; box-sizing: border-box; }
  html, body { width: 928px; height: 1200px; overflow: hidden; background: var(--paper); }
  body { font-family: "Arimo", Arial, sans-serif; color: var(--ink); }
  .letterhead { position: relative; width: 928px; height: 1200px; background: var(--paper); }

  .brand { position: absolute; left: 30px; top: 52px; display: flex; align-items: center; gap: 12px; }
  .brand-dot { width: 22px; height: 22px; border-radius: 50%; background: var(--brand-blue); }
  .brand-name { font-size: 27px; font-weight: 400; color: var(--brand-blue); letter-spacing: 0.2px; }

  .header-rule { position: absolute; left: 22px; top: 134px; width: 278px; height: 1.5px; background: var(--accent-orange); }
  .website { position: absolute; left: 36px; top: 142px; display: flex; align-items: center; gap: 10px;
             font-size: 14.5px; color: var(--brand-blue); }

  .salutation { position: absolute; left: 83px; top: 234px; font-size: 17px; color: var(--ink); }
  .letter-body { position: absolute; left: 155px; top: 271px; width: 706px; font-size: 16.6px; line-height: 20.4px; color: var(--ink); }
  .letter-body p { margin-bottom: 20.6px; }

  .signature { position: absolute; left: 78px; top: 910px; font-family: "Great Vibes", cursive; font-size: 52px; color: var(--ink-dark); }
  .signatory-role { position: absolute; left: 106px; top: 971px; font-size: 17px; color: var(--ink); }

  .footer-rule { position: absolute; left: 0; top: 1127px; width: 928px; height: 1.5px; background: var(--accent-orange); }
  .contact { position: absolute; top: 1140px; display: flex; align-items: flex-start; gap: 9px; font-size: 15px; line-height: 19px; color: var(--ink-dark); }
  .contact svg { flex: none; margin-top: 2px; }
  .contact-email { left: 64px; }
  .contact-phone { left: 414px; }
  .contact-address { left: 603px; }

  .tagline-band { position: absolute; left: 0; top: 1178px; width: 928px; height: 22px; background: var(--brand-green);
                  display: flex; align-items: center; justify-content: center; }
  .tagline { font-size: 12.5px; font-style: italic; color: var(--ink-dark); }
</style>
</head>
<body>
<div class="letterhead">
  <header>
    <div class="brand">
      <span class="brand-dot"></span>
      <span class="brand-name">TalkWell Consultants</span>
    </div>
    <div class="header-rule"></div>
    <div class="website">
      <svg width="18" height="18" viewBox="0 0 18 18" fill="none" stroke="var(--brand-blue)" stroke-width="1.5" aria-hidden="true">
        <circle cx="9" cy="9" r="7.5"/>
        <ellipse cx="9" cy="9" rx="3.2" ry="7.5"/>
        <line x1="1.5" y1="9" x2="16.5" y2="9"/>
        <path d="M3 4.8h12M3 13.2h12"/>
      </svg>
      <span>www.talkwellconsult.com</span>
    </div>
  </header>

  <main>
    <p class="salutation">Dear Sir / Madam,</p>
    <div class="letter-body">
      <p>Lorem ipsum dolor sit amet, consectetur adipisicing elit, sed do eiusmod tempor labore et olore magna aliqua. Ut enim ad minim veniam, quis nostrud exercitation ullamco laboris nisi ut aliquip ex ea commodo consequa.Lorem ipsum dolor sit amet, nsectetur adipisicing elit, sed do eiusmod tempor incididunt ut labore et dolore magna aliqua. Ut enim ad minim veniam, quis.</p>
      <p>Lorem ipsum dolor sit amet, consectetur adipisicing elit, sed do eiusmod tempor labore et dolore magna aliqua. Ut enim ad minim veniam, quis nostrud exercitation ullamco laboris nisi ut aliquip ex ea commodo consequa.Lorem ipsum dolor sit amet, nsectetur adipisicing elit, sed do eiusmod tempor incididunt ut labore et dolore magna aliqua. Ut enim ad minim veniam, quis.</p>
      <p>Lorem ipsum dolor sit amet, consectetur adipisicing elit, sed do eiusmod tempor labore et dolore magna aliqua. Ut enim ad minim veniam, quis nostrud exercitation ullamco laboris nisi ut aliquip ex ea commodo consequa.Lorem ipsum dolor sit amet, nsectetur adipisicing elit, sed do eiusmod tempor incididunt ut labore et dolore magna aliqua. Ut enim ad minim veniam, quis.</p>
      <p>Lorem ipsum dolor sit amet, consectetur adipisicing elit, sed do eiusmod tempor labore et dolore magna aliqua. Ut enim ad minim veniam, quis nostrud exercitation ullamco laboris nisi ut aliquip ex ea commodo consequa.Lorem ipsum dolor sit amet, nsectetur adipisicing elit, sed do eiusmod tempor incididunt ut labore et dolore magna aliqua. Ut enim ad minim veniam, quis.</p>
      <p>Lorem ipsum dolor sit amet, consectetur adipisicing elit, sed do eiusmod tempor labore et dolore magna aliqua. Ut enim ad minim veniam, quis nostrud exercitation ullamco laboris nisi ut aliquip ex ea commodo consequa.Lorem ipsum dolor sit amet, nsectetur adipisicing elit, sed do eiusmod tempor incididunt ut labore et dolore magna aliqua. Ut enim ad minim veniam, quis.</p>
    </div>
    <p class="signature">Your Name</p>
    <p class="signatory-role">Company Director</p>
  </main>

  <footer>
    <div class="footer-rule"></div>
    <div class="contact contact-email">
      <svg width="20" height="14" viewBox="0 0 20 14" aria-hidden="true">
        <rect x="0.5" y="0.5" width="19" height="13" rx="1.5" fill="var(--brand-blue)"/>
        <path d="M1.5 1.5 10 8l8.5-6.5" fill="none" stroke="var(--paper)" stroke-width="1.4"/>
      </svg>
      <span>name@talkwellconsult.com</span>
    </div>
    <div class="contact contact-phone">
      <svg width="16" height="16" viewBox="0 0 24 24" aria-hidden="true">
        <path fill="var(--brand-blue)" d="M6.6 10.8a15.1 15.1 0 0 0 6.6 6.6l2.2-2.2c.3-.3.7-.4 1-.2 1.1.4 2.3.6 3.6.6.6 0 1 .4 1 1V20c0 .6-.4 1-1 1A17 17 0 0 1 3 4c0-.6.4-1 1-1h3.5c.6 0 1 .4 1 1 0 1.3.2 2.5.6 3.6.1.3 0 .7-.2 1z"/>
      </svg>
      <span>000 000 00</span>
    </div>
    <div class="contact contact-address">
      <svg width="12" height="17" viewBox="0 0 12 17" aria-hidden="true">
        <path fill="var(--brand-blue)" d="M6 0a6 6 0 0 0-6 6c0 4.5 6 11 6 11s6-6.5 6-11a6 6 0 0 0-6-6zm0 8.3A2.3 2.3 0 1 1 6 3.7a2.3 2.3 0 0 1 0 4.6z"/>
      </svg>
      <address style="font-style: normal;">5345 Any Street west,<br>Townsvlle, ST&nbsp; 54321</address>
    </div>
    <div class="tagline-band">
      <span class="tagline">Helping Children Earlier to Succeed Latter</span>
    </div>
  </footer>
</div>
</body>
</html>
```